Design B2B Video-Website
Zielgruppe
Das entstehende Portal bietet Videos zum Streaming an und richtet sich an Geschäftskunden, stellt also einen Shop mit Login dar. Das Angebot der Videos ist offen einsehbar, das Streamen ist gegen Bezahlung im Shop zu erwerben.
Aufgabenstellung
Die Seite soll sich im Layout an postqually.com orientieren; das Farbschema angelehnt an folgende
Hexcodes:
#231f20, #60bb46 und #828282 (und ähnliche Töne). Sprache ist Deutsch.
1. Startseite/Allgemein
Die dortige Navigationsleiste oben soll etwas größer werden; wird erweitert duch ein Logo links (muss NICHT designt werden; bitte mit Platzhalter füllen); die Navigationsitems (Angebot, Preise, Über uns, FAQ, Blog), mit Farb-hover-Effekt, sollen eine Kombination aus kleine Icon und Text sein; auf der rechten Seite die Buttons "Anmelden" (nicht rot), "Login" und Suchfenster mit Lupe und "Suche". Ein Zusatzmenü wie beim Klick auf "More"
soll mitdesigned werden (Items können Platzhalter sein).
Im Hauptteil eine Box mit Auflistung von Videos (auch zum Ansehen).
Die Seite enthält ebenso einen deutlichen Footer (umfangreicher).
2. Unterseite
Inhalt der Unterseite kann beispielhaft von "Features" bzw. "Pricing" entnommen werden. Dazu hell-grauer Hintergrund (verlaufend), mit eingepassten Bildern.
"Login"-Fenster bzw. "Anmelden" ähnlich zu Postqually; mehr Felder und Farbschema siehe oben.
3.Login-Bereich
Im Login-Bereich (sprich wenn der Nutzer eingeloggt ist), soll die Navigation (mit anderen Items) nach links wandern und vertikal angeordnet werden. Im Hauptinhalt(rechts von der Navigation) sollen dann die Videos oder anderen Inhalte dargestellt werden.

```html
<!DOCTYPE html>
<html lang="de">
<head>
<meta charset="utf-8">
<title>Video B2B – Startseite</title>
<link href="https://fonts.googleapis.com/css2?family=Open+Sans:wght@400;600&family=Source+Sans+3:wght@400;600;700&display=swap" rel="stylesheet">
<style>
:root{
  --ink:#231f20;
  --green:#60bb46;
  --grey:#828282;
  --hero-bg:#efefef;
  --line:#dcdcdc;
  --bezel:#0c0c0c;
  --chin:#c9c9cb;
  --screen:#7b7c84;
  --panel:#f2f2f2;
}
*{margin:0;padding:0;box-sizing:border-box}
html,body{width:1200px;height:1073px;overflow:hidden;background:#fff}
body{position:relative;font-family:"Open Sans",sans-serif;color:var(--ink)}
.abs{position:absolute}

/* header */
.site-header{position:absolute;left:0;top:0;width:1200px;height:75px;background:#fff;border-bottom:1px solid var(--line)}
.brand{position:absolute;left:207px;top:20px;font-size:29px;font-weight:400;color:var(--ink);letter-spacing:.5px}
.nav-item{position:absolute;top:0;height:75px;display:flex;flex-direction:column;align-items:center;justify-content:center;gap:4px;font-size:13px;color:var(--ink);transform:translateX(-50%)}
.nav-item svg{width:20px;height:20px}
.nav-item.active{background:var(--green);color:#fff;width:66px;transform:none}
.nav-item.small{font-size:11px}

/* hero */
.hero-band{position:absolute;left:0;top:76px;width:1200px;height:426px;background:var(--hero-bg)}
.hero-title{position:absolute;left:0;width:1130px;top:110px;text-align:center;font-size:25px;font-weight:400;letter-spacing:.3px}
.prop{position:absolute;border-radius:10px}
.prop-clock{left:136px;top:126px;width:111px;height:124px;border-radius:50%;background:radial-gradient(circle,#fff 55%,#d8d8d8 70%,#bdbdbd)}
.prop-tablet{left:92px;top:461px;width:190px;height:247px;background:linear-gradient(160deg,#2a2a2a 0%,#555 45%,#eaeaea 70%,#f4f4f4)}
.prop-books{left:923px;top:474px;width:158px;height:152px;background:linear-gradient(180deg,#3a3a3a,#8d4b2c 50%,#d8c9b0)}
.prop-desk{left:900px;top:590px;width:206px;height:143px;background:linear-gradient(120deg,#d9d9d9,#f3c23a 55%,#f2f2f2)}

.monitor{position:absolute;left:216px;top:167px;width:707px;height:488px;border-radius:14px;background:var(--bezel);overflow:hidden}
.monitor-chin{position:absolute;left:0;bottom:0;width:100%;height:65px;background:linear-gradient(180deg,#d4d4d6,#bdbdbf)}
.monitor-stand{position:absolute;left:461px;top:655px;width:215px;height:78px;background:linear-gradient(90deg,#b9b9b9,#ececec 50%,#b0b0b0);clip-path:polygon(8% 0,92% 0,100% 100%,0 100%);border-radius:0 0 8px 8px}
.screen{position:absolute;left:28px;top:28px;width:650px;height:366px;background:var(--screen)}
.video{position:absolute;left:30px;top:14px;width:581px;height:246px;background:radial-gradient(ellipse at center,#f4f4f4 0%,#cfcfd2 70%,#a9a9ad 100%)}
.player{position:absolute;left:30px;top:260px;width:581px;height:29px;background:#fff;display:flex;align-items:center}
.player-play{width:91px;height:29px;border-right:2px solid #7a7a7a;display:flex;align-items:center;justify-content:center}
.player-track{position:relative;flex:1;height:29px}
.player-track .rail{position:absolute;left:28px;right:21px;top:13px;height:3px;background:#e4e4e4}
.player-track .knob{position:absolute;left:21px;top:7px;width:15px;height:15px;border-radius:50%;background:var(--green)}
.video-meta{position:absolute;left:30px;top:311px;width:581px;height:34px;background:var(--panel);display:flex;align-items:center}
.avatar{width:34px;height:34px;background:linear-gradient(180deg,#9fd0e0,#e4a26f)}
.meta-text{margin-left:7px;flex:1;font-family:"Source Sans 3",sans-serif}
.meta-text b{display:block;font-weight:400;font-size:10.5px;color:#333}
.meta-text span{display:block;font-size:7.5px;color:#333;margin-top:-1px}
.stat{width:35px;height:34px;margin-left:1px;background:#fff;display:flex;flex-direction:column;align-items:center;justify-content:center;gap:2px;font-size:8.5px;color:#666;font-family:"Source Sans 3",sans-serif}
.stat:last-child{margin-right:4px}
.stat svg{width:10px;height:10px}

/* call to action */
.cta-text{position:absolute;left:220px;top:789px;width:430px;text-align:center;font-size:14.5px;line-height:18px}
.cta-button{position:absolute;left:662px;top:786px;width:158px;height:42px;background:var(--green);color:#233f1a;font-size:19px;display:flex;align-items:center;justify-content:center}

/* footer */
.footer{font-family:"Source Sans 3",sans-serif}
.f-head{position:absolute;font-size:12.5px;font-weight:600;color:#333;letter-spacing:.2px}
.f-sub{position:absolute;left:190px;top:957px;font-size:10px;color:#333}
.f-input{position:absolute;left:190px;top:978px;width:182px;height:22px;border:1px solid #d6d6d0;background:#fcfbf7;font-size:10px;color:#444;padding:5px 0 0 11px}
.f-link{position:absolute;font-size:10px;color:#333}
.social{position:absolute;top:961px;width:33px;height:33px;border-radius:50%;background:#2b2b2b;color:#fff;font-size:8px;display:flex;align-items:center;justify-content:center}
.copyright{position:absolute;left:0;width:1144px;top:1042px;text-align:center;font-size:9.5px;color:#333}
</style>
</head>
<body>

<header class="site-header">
  <div class="brand">MyLogo</div>
  <nav>
    <a class="nav-item active" style="left:327px">
      <svg viewBox="0 0 20 20" fill="none" stroke="#fff" stroke-width="1.3"><path d="M2 7l8-4 8 4-8 4z"/><path d="M2 10l8 4 8-4"/><path d="M2 13l8 4 8-4"/></svg>Angebot</a>
    <a class="nav-item" style="left:437px">
      <svg viewBox="0 0 20 20" fill="none" stroke="#60bb46" stroke-width="1.3"><rect x="3" y="3" width="14" height="15"/><path d="M3 7h14"/><g fill="#60bb46" stroke="none"><rect x="5" y="9" width="2" height="2"/><rect x="9" y="9" width="2" height="2"/><rect x="13" y="9" width="2" height="2"/><rect x="5" y="13" width="2" height="2"/><rect x="9" y="13" width="2" height="2"/><rect x="13" y="13" width="2" height="2"/></g></svg>Preise</a>
    <a class="nav-item" style="left:520px">
      <svg viewBox="0 0 20 20" fill="#60bb46"><circle cx="11" cy="3" r="2"/><path d="M8 8h4l-2 9h2l-1 1H7l2-8H8z"/></svg>Über uns</a>
    <a class="nav-item" style="left:593px">
      <svg viewBox="0 0 20 20" fill="none" stroke="#60bb46" stroke-width="2.4"><path d="M5 6a5 4 0 1 1 6 4c-1 1-1 2-1 4"/><circle cx="10" cy="18" r=".6" fill="#60bb46"/></svg>FAQ</a>
    <a class="nav-item" style="left:660px">
      <svg viewBox="0 0 20 20" fill="none" stroke="#60bb46" stroke-width="1.3"><path d="M3 17l1-4L14 3l3 3L7 16z"/><path d="M12 5l3 3"/></svg>Blog</a>
    <a class="nav-item small" style="left:775px">
      <svg viewBox="0 0 20 20" fill="#60bb46"><circle cx="10" cy="5" r="3.5"/><path d="M4 19c0-7 2-10 6-10s6 3 6 10z"/></svg>Anmelden</a>
    <a class="nav-item small" style="left:844px">
      <svg viewBox="0 0 20 20" fill="#60bb46"><path d="M6 9V6a4 4 0 0 1 8 0v3h-2V6a2 2 0 0 0-4 0v3z"/><rect x="4" y="9" width="12" height="10"/></svg>Login</a>
    <a class="nav-item small" style="left:907px">
      <svg viewBox="0 0 20 20" fill="none" stroke="#60bb46" stroke-width="2.4"><circle cx="7" cy="7" r="4.5"/><path d="M10.5 10.5l7 7" stroke-width="3"/></svg>Suche</a>
  </nav>
</header>

<section class="hero">
  <div class="hero-band"></div>
  <h1 class="hero-title">Videos für komplexe B2B-Themen.</h1>
  <div class="prop prop-clock" role="img" aria-label="Wanduhr"></div>
  <div class="prop prop-tablet" role="img" aria-label="Tablet auf Papierblättern mit Kugelschreiber"></div>
  <div class="prop prop-books" role="img" aria-label="Stapel Bücher"></div>
  <div class="prop prop-desk" role="img" aria-label="Taschenrechner und Becher mit Bleistiften"></div>

  <div class="monitor-stand"></div>
  <div class="monitor">
    <div class="screen">
      <div class="video" role="img" aria-label="Videovorschau mit 3D-Schriftzug und grünen Splittern"></div>
      <div class="player">
        <div class="player-play"><svg width="13" height="14" viewBox="0 0 13 14"><path d="M0 0l13 7-13 7z" fill="#60bb46"/></svg></div>
        <div class="player-track"><div class="rail"></div><div class="knob"></div></div>
      </div>
      <div class="video-meta">
        <div class="avatar" role="img" aria-label="Profilbild des Anbieters"></div>
        <div class="meta-text"><b>B2B Marketing</b><span>Solution</span></div>
        <div class="stat"><svg viewBox="0 0 10 10"><path d="M5 0l1.5 3.3 3.5.3-2.7 2.3.9 3.5L5 7.5 1.8 9.4l.9-3.5L0 3.6l3.5-.3z" fill="#60bb46"/></svg>3.6</div>
        <div class="stat"><svg viewBox="0 0 10 10" fill="#60bb46"><rect x="0" y="4" width="2.5" height="6"/><path d="M3 4l2-4c1 0 1.5.7 1.3 2L6 4h3.5l-1 6H3z"/></svg>27</div>
        <div class="stat"><svg viewBox="0 0 10 10"><path d="M5 1C2 1 0 2.7 0 4.6c0 1.2.8 2.2 2 2.8L1.5 10 4 8.2c.3 0 .7.1 1 .1 3 0 5-1.7 5-3.7S8 1 5 1z" fill="#60bb46"/></svg>27</div>
      </div>
    </div>
    <div class="monitor-chin"></div>
  </div>
</section>

<section class="cta">
  <p class="cta-text">Lorem ipsum dolor sit amet, consetetur sadipscing elitr,<br>sed diam nonumy eirmod tempor invidunt ut</p>
  <a class="cta-button">Anmelden</a>
</section>

<footer class="footer">
  <h3 class="f-head" style="left:190px;top:937px">NEWSLETTER ANMELDUNG</h3>
  <p class="f-sub">Verpassen Sie keine Neuigkeiten mehr</p>
  <div class="f-input">E-Mail Adresse eingeben</div>

  <h3 class="f-head" style="left:496px;top:931px">LINKS</h3>
  <a class="f-link" style="left:498px;top:951px">Impressum</a>
  <a class="f-link" style="left:498px;top:972px">Kontakt</a>
  <a class="f-link" style="left:498px;top:993px">Blog</a>
  <a class="f-link" style="left:602px;top:951px">AGB</a>
  <a class="f-link" style="left:602px;top:972px">Über uns</a>
  <a class="f-link" style="left:602px;top:993px">FAQ</a>

  <h3 class="f-head" style="left:786px;top:931px">SIE FINDEN UNS AUCH AUF:</h3>
  <a class="social" style="left:786px">Fazo</a>
  <a class="social" style="left:830px">Tubio</a>
  <a class="social" style="left:871px">Pipro</a>

  <p class="copyright">©2001-2013 All Rights Reserved. Video B2B&nbsp; is a registered trademark of&nbsp; Video Group</p>
</footer>

</body>
</html>
```